design a catchy flyer for my electrical buisness

need a flyer designed to attract people to my business by looking professional and offering specials

Target Market(s)

all people i want to look affordable to everyone but still keeping that professional look and feel

Industry/Entity Type

Electrical

Requirements
Must have
• NO JOB TO BIG OR SMALL
• CALL NOW FOR A FREE QUOTE 0400318726
• NO CALL OUT FEE
• same promises as uploaded pic maybe written different style
• Your neighborhood electrician
• 100% satisfaction guaranteed
• were here to help
• mention this flyer for 10% off
• specializing in house renovations, extensions, kitchen and bathroom upgrades switchboard upgrades
• Make your house safe with our RCD and smoke alarm packages
Nice to have
• modern
• proffesional
• shows trust when customers read it
Should not have
• corny slogans
• cheap look

```html
<!DOCTYPE html>
<html lang="en">
<head>
<meta charset="utf-8">
<title>Your Neighborhood Electrician – VoltHaven</title>
<link rel="stylesheet" href="https://fonts.googleapis.com/css2?family=Oswald:wght@400;500;600&family=Open+Sans:wght@400;600;700&family=Roboto+Condensed:wght@400&display=swap">
<style>
  :root {
    --orange: #f07f1f;
    --charcoal: #545657;
    --ink: #141414;
    --text-grey: #3f4142;
    --white: #ffffff;
    --photo-a: #8a9a8c;
    --photo-b: #d8d2c4;
  }
  * { box-sizing: border-box; margin: 0; padding: 0; }
  html, body { width: 960px; height: 1200px; overflow: hidden; background: #f2f2f2; }
  .flyer {
    position: relative; width: 960px; height: 1200px; overflow: hidden;
    background: var(--orange);
    font-family: "Open Sans", Arial, sans-serif;
  }
  .headline {
    position: absolute; top: 18px; left: 0; width: 960px; text-align: center;
    font-family: "Oswald", "Arial Narrow", sans-serif; font-weight: 600;
    font-size: 60px; line-height: 70px; letter-spacing: 1px; color: var(--white);
  }
  .headline .accent { color: var(--ink); }
  .hero-photo {
    position: absolute; top: 100px; left: 0; width: 900px; height: 375px;
    border-top-right-radius: 70px;
    background: linear-gradient(120deg, var(--photo-a), var(--photo-b) 55%, #b7a98a);
  }
  .hero-photo-strip {
    position: absolute; top: 470px; left: 0; width: 90px; height: 184px;
    background: linear-gradient(180deg, #b9c07a, #8a9a60);
  }
  .help-tab {
    position: absolute; top: 352px; left: 620px; width: 340px; height: 60px;
    background: var(--white); border-radius: 30px 0 0 30px;
    font-family: "Oswald", "Arial Narrow", sans-serif; font-weight: 500;
    font-size: 36px; line-height: 60px; color: var(--orange); padding-left: 24px;
  }
  .offer-panel {
    position: absolute; top: 475px; left: 90px; width: 870px; height: 395px;
    background: var(--white); border-top-left-radius: 80px;
    box-shadow: -3px -3px 0 #cfcfcf;
  }
  .lower-white {
    position: absolute; top: 697px; left: 0; width: 960px; height: 173px;
    background: var(--white);
  }
  .brand {
    position: absolute; top: 522px; left: 150px; display: flex; align-items: center; gap: 20px;
  }
  .brand-dot { width: 64px; height: 64px; border-radius: 50%; background: var(--orange); }
  .brand-name {
    font-family: "Open Sans", Arial, sans-serif; font-weight: 400;
    font-size: 38px; color: var(--orange);
  }
  .tagline-pill {
    position: absolute; top: 602px; left: 90px; width: 520px; height: 42px;
    background: var(--charcoal); border-radius: 0 21px 21px 0;
    font-family: "Oswald", "Arial Narrow", sans-serif; font-size: 25px; line-height: 42px;
    color: var(--white); padding-left: 24px; white-space: nowrap;
  }
  .tagline-pill .sep { color: var(--orange); padding: 0 8px; }
  .discount-badge { position: absolute; top: 439px; left: 700px; width: 226px; height: 226px; }
  .badge-text {
    position: absolute; top: 500px; left: 700px; width: 226px; text-align: center; color: var(--ink);
    white-space: nowrap;
  }
  .badge-text .b1 { font-size: 30px; line-height: 36px; }
  .badge-text .b2 { font-size: 20px; line-height: 26px; }
  .badge-text .b3 { font-size: 36px; line-height: 46px; font-weight: 700; color: var(--white); }
  .specialties { position: absolute; top: 665px; left: 90px; width: 400px; }
  .section-title {
    font-weight: 700; font-size: 24px; color: var(--text-grey); text-align: center; margin-bottom: 12px;
  }
  .specialties ul { list-style: none; }
  .specialties li {
    display: flex; align-items: center; gap: 10px;
    font-family: "Oswald", "Arial Narrow", sans-serif; font-size: 26px; line-height: 34px;
    color: var(--orange); white-space: nowrap; letter-spacing: -0.3px;
  }
  .tick { width: 18px; height: 18px; flex: none; }
  .divider {
    position: absolute; top: 660px; left: 511px; width: 2px; height: 190px; background: var(--orange);
  }
  .safety { position: absolute; top: 665px; left: 545px; width: 400px; }
  .safety h2 {
    font-family: "Oswald", "Arial Narrow", sans-serif; font-weight: 400;
    font-size: 28px; color: var(--orange); white-space: nowrap;
  }
  .safety ul { list-style: none; margin: 26px 0 0 107px; }
  .safety li {
    position: relative; padding-left: 22px; font-weight: 600; font-size: 22px;
    line-height: 27px; color: var(--text-grey); margin-bottom: 12px;
  }
  .safety li::before {
    content: ""; position: absolute; left: 0; top: 10px; width: 8px; height: 8px;
    border-radius: 50%; background: var(--orange);
  }
  .promise {
    position: absolute; top: 860px; left: 0; width: 960px; height: 264px;
    background: var(--charcoal); border-top: 8px solid var(--orange);
  }
  .promise-tab {
    position: absolute; top: 868px; left: 163px; width: 630px; height: 62px;
    background: var(--orange); border-radius: 0 0 30px 30px;
    box-shadow: 0 4px 0 #cfcfcf;
    font-family: "Oswald", "Arial Narrow", sans-serif; font-weight: 500;
    font-size: 32px; line-height: 62px; letter-spacing: 3px; color: var(--white); text-align: center;
  }
  .guarantee-seal {
    position: absolute; top: 952px; left: 43px; width: 136px; height: 136px; border-radius: 50%;
    background: var(--white); border: 5px solid var(--charcoal); box-shadow: 0 0 0 3px var(--white);
    display: flex; flex-direction: column; align-items: center; justify-content: center;
    transform: rotate(-8deg); font-family: "Oswald", "Arial Narrow", sans-serif; color: var(--charcoal);
  }
  .guarantee-seal .pct { font-size: 30px; line-height: 32px; font-weight: 600; }
  .guarantee-seal .lbl { font-size: 15px; line-height: 17px; text-align: center; }
  .promise-list {
    position: absolute; top: 943px; left: 240px; list-style: none;
    font-family: "Roboto Condensed", "Arial Narrow", sans-serif; font-size: 21px; line-height: 28.5px;
    color: var(--white);
  }
  .promise-list li::before { content: "•"; padding-right: 8px; }
  .cta-bar {
    position: absolute; top: 1124px; left: 0; width: 960px; height: 76px;
    background: var(--orange); border-top: 4px solid #e8e8e8;
    display: flex; align-items: center; justify-content: space-between; padding: 0 32px 0 33px;
    font-size: 34px; color: var(--ink); white-space: nowrap;
  }
  .cta-bar strong { font-weight: 700; }
  .cta-bar .free { color: var(--white); font-weight: 700; padding-left: 10px; }
  .cta-bar .phone { font-weight: 700; font-size: 40px; }
</style>
</head>
<body>
<main class="flyer">
  <h1 class="headline">YOUR NEIGHBORHOOD <span class="accent">ELECTRICIAN</span></h1>

  <div class="hero-photo" role="img" aria-label="Photo of an electrician in a hard hat and safety vest working on a switchboard"></div>
  <div class="hero-photo-strip" role="img" aria-label="Continuation of the electrician photo"></div>
  <div class="help-tab">WERE HERE TO HELP</div>

  <section class="offer-panel"></section>
  <div class="lower-white"></div>

  <div class="brand">
    <span class="brand-dot"></span>
    <span class="brand-name">VoltHaven</span>
  </div>
  <div class="tagline-pill">NO JOB TO BIG OR SMALL<span class="sep">|</span>NO CALL OUT FEE</div>

  <svg class="discount-badge" viewBox="0 0 200 200" aria-hidden="true">
    <polygon fill="#f07f1f" stroke="#ffffff" stroke-width="2"
      points="100,3 114.8,16.3 133.2,8.8 142.5,26.4 162.4,25.7 165.1,45.3 184,51.5 179.9,70.9 195.5,83.2 185,100 195.5,116.8 179.9,129.1 184,148.5 165.1,154.7 162.4,174.3 142.5,173.6 133.2,191.2 114.8,183.7 100,197 85.2,183.7 66.8,191.2 57.5,173.6 37.6,174.3 34.9,154.7 16,148.5 20.1,129.1 4.5,116.8 15,100 4.5,83.2 20.1,70.9 16,51.5 34.9,45.3 37.6,25.7 57.5,26.4 66.8,8.8 85.2,16.3"/>
  </svg>
  <div class="badge-text">
    <div class="b1">Mention</div>
    <div class="b2">this flyer for</div>
    <div class="b3">10% OFF</div>
  </div>

  <section class="specialties">
    <h2 class="section-title">Specializing in</h2>
    <ul>
      <li><svg class="tick" viewBox="0 0 20 20"><circle cx="10" cy="10" r="8" fill="none" stroke="#545657" stroke-width="2"/><path d="M6 10l3 3 8-8" fill="none" stroke="#545657" stroke-width="2"/></svg>HOUSE RENOVATIONS</li>
      <li><svg class="tick" viewBox="0 0 20 20"><circle cx="10" cy="10" r="8" fill="none" stroke="#545657" stroke-width="2"/><path d="M6 10l3 3 8-8" fill="none" stroke="#545657" stroke-width="2"/></svg>EXTENSIONS</li>
      <li><svg class="tick" viewBox="0 0 20 20"><circle cx="10" cy="10" r="8" fill="none" stroke="#545657" stroke-width="2"/><path d="M6 10l3 3 8-8" fill="none" stroke="#545657" stroke-width="2"/></svg>KITCHEN AND BATHROOM UPGRADES</li>
      <li><svg class="tick" viewBox="0 0 20 20"><circle cx="10" cy="10" r="8" fill="none" stroke="#545657" stroke-width="2"/><path d="M6 10l3 3 8-8" fill="none" stroke="#545657" stroke-width="2"/></svg>SWITCHBOARD UPGRADES</li>
    </ul>
  </section>
  <div class="divider"></div>
  <section class="safety">
    <h2>MAKE YOUR HOUSE SAFE WITH OUR</h2>
    <ul>
      <li>RCD</li>
      <li>Smoke alarm<br>packages</li>
    </ul>
  </section>

  <section class="promise"></section>
  <div class="promise-tab">OUR PROMISE TO YOU...</div>
  <div class="guarantee-seal">
    <span class="pct">100%</span>
    <span class="lbl">SATISFACTION<br>GUARANTEED</span>
  </div>
  <ul class="promise-list">
    <li>Before any job begins you will know the exact cost.</li>
    <li>Fixed price guarantee assuring no extra costs.</li>
    <li>We will live your place as clean as when we arrived.</li>
    <li>We will return your telephone calls promptly.</li>
    <li>We will provide a 12 Month warranty on all parts.</li>
    <li>We will provide friendly, helpful sevice and advice.</li>
  </ul>

  <footer class="cta-bar">
    <span><strong>CALL NOW</strong> FOR A <span class="free">FREE QUOTE</span></span>
    <span class="phone">0400 318 726</span>
  </footer>
</main>
</body>
</html>
```